I need 3 labels for the botteled coffees we are about to launch.

We are launching our very own botteled cold brewed coffees. There will be 3 variants: black, simple cold brew, milk and chocolate cold brew and caramel cold brew. All 3 labels must have the same design principle, use only 1 font and have our logo on it and date of botteling (data imbutelierii - romanian) with a light square next to it so that we can write the date down).
I have attached some cold brew bottle designs that I found over the internet.
You can find the bottle we will use on http://velmora.com.ro/sticle-cilindrice/ product name is Sticla 300ml KX52 and it have the dimensions as well.

If you have any more questions feel free to ask. As for our company image I recommend you visit our social media sites from www.brivanel.ro

Cheers

```html
<!DOCTYPE html>
<html lang="en">
<head>
<meta charset="utf-8">
<title>Brivanel – Label Design First Entry</title>
<link rel="stylesheet" href="https://fonts.googleapis.com/css2?family=Arvo:ital,wght@0,400;0,700;1,700&display=swap">
<style>
  :root {
    --band: #1a0d08;
    --paper: #ffffff;
    --brown: #6b3a22;
    --badge: #7a4a33;
    --label-dark: #34220f;
    --label-gold: #c9a46a;
    --accent-yellow: #f2c21b;
    --glass-light: #f4f6f7;
    --glass-mid: #dde2e5;
    --glass-edge: #b9c0c4;
  }
  * { margin: 0; padding: 0; box-sizing: border-box; }
  html, body { width: 1200px; height: 675px; overflow: hidden; background: var(--paper); }
  .board {
    position: relative;
    width: 1200px; height: 675px;
    background: var(--paper);
    font-family: "Arvo", Georgia, serif;
  }
  .top-band {
    position: absolute; left: 0; top: 0;
    width: 100%; height: 24px;
    background: var(--band);
  }
  .entry-title {
    position: absolute; left: 133px; top: 148px;
    color: var(--brown);
    font-weight: 700; font-style: italic;
    font-size: 50px; line-height: 62px;
    letter-spacing: 0.5px;
  }
  .brand-badge {
    position: absolute; left: 162px; top: 343px;
    width: 228px; height: 228px;
    border-radius: 50%;
    background: var(--badge);
    display: flex; align-items: center; justify-content: center;
    color: var(--paper);
    font-size: 30px; font-weight: 400;
    letter-spacing: 2px;
  }
  .bottle {
    position: absolute; left: 740px; top: 92px;
    width: 200px; height: 520px;
  }
  .bottle-label {
    position: absolute; left: 757px; top: 327px;
    width: 167px; height: 200px;
    background: var(--label-dark);
    overflow: hidden;
  }
  .label-brand {
    position: absolute; left: 50%; top: 14px;
    transform: translateX(-50%);
    width: 44px; height: 44px;
    border-radius: 50%;
    border: 1px solid var(--label-gold);
    display: flex; align-items: center; justify-content: center;
    color: var(--label-gold);
    font-size: 6.5px; letter-spacing: 0.5px;
  }
  .label-artwork {
    position: absolute; left: 30px; top: 64px;
    width: 100px; height: 92px;
    border-radius: 50%;
    background: radial-gradient(circle at 50% 45%, #b8905a 0%, #8a6a3e 55%, #4a3219 100%);
  }
  .label-variant {
    position: absolute; right: 16px; top: 148px;
    color: var(--accent-yellow);
    font-weight: 700; font-style: italic;
    font-size: 17px; letter-spacing: 0.5px;
  }
</style>
</head>
<body>
<main class="board">
  <div class="top-band"></div>

  <h1 class="entry-title">Label Design<br>First Entry</h1>

  <div class="brand-badge">BRIVANEL</div>

  <svg class="bottle" viewBox="0 0 200 520" role="img" aria-label="Product photo of a clear 300 ml glass bottle">
    <defs>
      <linearGradient id="glass" x1="0" x2="1" y1="0" y2="0">
        <stop offset="0" stop-color="#c9cfd2"/>
        <stop offset="0.2" stop-color="#f4f6f7"/>
        <stop offset="0.5" stop-color="#e6eaec"/>
        <stop offset="0.8" stop-color="#f7f8f9"/>
        <stop offset="1" stop-color="#bfc6ca"/>
      </linearGradient>
    </defs>
    <path d="M66 6 H134 V40 C134 90 184 120 186 190 V480 Q186 496 170 496 H30 Q14 496 14 480 V190 C16 120 66 90 66 40 Z"
          fill="url(#glass)" stroke="#b9c0c4" stroke-width="1.5"/>
    <ellipse cx="100" cy="510" rx="70" ry="6" fill="#eef0f1"/>
  </svg>

  <section class="bottle-label" aria-label="Cold brew label – Black variant">
    <div class="label-brand">BRIVANEL</div>
    <div class="label-artwork" role="img" aria-label="Illustration of a coffee bean with a ribbon banner"></div>
    <div class="label-variant">BLACK</div>
  </section>
</main>
</body>
</html>
```